Real Estate agent needs flyer/folder to contain bio and overview of services

I'm including files of the layout of the small folder. The folder is 6 1/2 across and 9 1/2 inches long. It will have a front & back cover and then writing on the 2 inside pages.

I am sending a few files to incorporate into the flyer, 1 new logo to use and 2 files which are coloring ideas.

```html
<!DOCTYPE html>
<html lang="en">
<head>
<meta charset="utf-8">
<title>Dana Moretti – Realtor Folder</title>
<link href="https://fonts.googleapis.com/css2?family=Roboto+Slab:wght@600&family=PT+Serif:ital,wght@0,400;0,700;1,400&family=Open+Sans:wght@400;600&display=swap" rel="stylesheet">
<style>
  :root{
    --blue:#2f5eb0;
    --blue-deep:#1f4a98;
    --blue-light:#6e93d1;
    --ink:#333a44;
    --grey-text:#555a60;
    --paper:#ffffff;
    --stage:#ececec;
    --photo-pool-a:#c9ced6;
    --photo-pool-b:#eef0f3;
    --photo-night-a:#3b3f4a;
    --photo-palm-a:#7aa0c9;
    --photo-palm-b:#b9976a;
  }
  *{box-sizing:border-box;margin:0;padding:0}
  html,body{width:1200px;height:546px;overflow:hidden;background:var(--stage)}
  .canvas{position:relative;width:1200px;height:546px;overflow:hidden;background:var(--stage);font-family:"PT Serif",Georgia,serif;color:var(--ink)}

  /* ---------- outside: back cover ---------- */
  .back-cover{position:absolute;left:66px;top:82px;width:260px;height:382px;background:var(--paper);overflow:hidden}
  .back-cover svg.shapes{position:absolute;inset:0}
  .brand{position:absolute;left:14px;top:60px;display:flex;align-items:center;gap:4px;font:700 9px "PT Serif",Georgia,serif;color:var(--blue)}
  .brand .dot{width:8px;height:8px;border-radius:50%;background:var(--blue)}
  .agent-mark{position:absolute;left:100px;top:64px;font:400 21px "PT Serif",Georgia,serif;color:var(--blue);letter-spacing:.3px}
  .lifelong-note{position:absolute;left:14px;top:138px;width:122px;font:700 5.2px/7px "Open Sans",Arial,sans-serif;color:#3b4a66}
  .headshot{position:absolute;left:4px;top:196px;width:102px;height:142px}
  .agent-id{position:absolute;left:108px;top:262px;font:400 7px/9px "Open Sans",Arial,sans-serif;color:#4a4f57}
  .agent-id .dre{font-size:5.5px}
  .agent-invite{position:absolute;left:108px;top:290px;font:italic 400 7px/8.5px "PT Serif",Georgia,serif;color:#2a2f36}
  .contact{position:absolute;left:14px;top:334px;color:#fff;font:400 6.2px/10.5px "Open Sans",Arial,sans-serif}
  .contact .name{font-weight:600;font-size:8px;letter-spacing:.4px;margin-bottom:1px}
  .contact li{list-style:none;display:flex;align-items:center;gap:5px}
  .contact svg{width:7px;height:7px}
  .badges{position:absolute;left:204px;top:350px;display:flex;gap:6px}
  .badges span{width:13px;height:14px;background:#cfd6e4;opacity:.85}

  /* ---------- outside: front cover ---------- */
  .front-cover{position:absolute;left:326px;top:82px;width:236px;height:382px;background:var(--paper);clip-path:path('M0 0 H214 Q240 191 214 382 H0 Z')}
  .front-cover svg.shapes{position:absolute;inset:0}
  .front-mark{position:absolute;left:0;width:220px;top:178px;text-align:center;font:400 24px "PT Serif",Georgia,serif;color:var(--blue)}
  .news-title{position:absolute;left:16px;top:332px;font:700 20px/21px "PT Serif",Georgia,serif;color:var(--grey-text)}

  /* ---------- inside ---------- */
  .inside-photo{position:absolute;left:632px;top:82px;width:112px;height:382px;clip-path:path('M28 0 H112 V382 H28 Q-6 191 28 0 Z')}
  .inside-photo svg{width:100%;height:100%}
  .inside-page{position:absolute;left:744px;top:82px;width:396px;height:382px;background:var(--paper)}
  .section{position:absolute}
  .section h2{font:600 10.2px/12.5px "Roboto Slab",Georgia,serif;color:var(--blue);letter-spacing:.3px;margin-bottom:7px}
  .section p{font:400 5.1px/6.3px "PT Serif",Georgia,serif;color:#2c2f33;text-align:justify;margin-bottom:5px}
  .intro{left:4px;top:22px;width:124px}
  .tenet{left:4px;top:186px;width:124px}
  .tenet h2{margin-bottom:6px}
  .services{left:4px;top:264px;width:124px}
  .selling{left:150px;top:22px;width:112px}
  .buying{left:272px;top:22px;width:114px}

  .testimonials{position:absolute;left:134px;top:220px;width:262px;height:162px;background:var(--blue);color:#fff;text-align:center;padding:13px 14px 0}
  .testimonials h2{font:600 10px "Roboto Slab",Georgia,serif;letter-spacing:.6px;margin-bottom:6px}
  .testimonials blockquote{font:400 5.1px/6.5px "PT Serif",Georgia,serif;margin-bottom:7px}
  .testimonials cite{display:block;font-style:normal;font-weight:700;font-size:6.2px;margin-top:2px}
</style>
</head>
<body>
<div class="canvas">

  <!-- back cover -->
  <section class="back-cover">
    <svg class="shapes" width="260" height="382" viewBox="0 0 260 382">
      <defs>
        <linearGradient id="poolRoom" x1="0" y1="0" x2="1" y2="1">
          <stop offset="0" stop-color="var(--photo-pool-b)"/>
          <stop offset="1" stop-color="var(--photo-pool-a)"/>
        </linearGradient>
      </defs>
      <polygon role="img" aria-label="Photo of a modern home interior opening onto a pool" points="0,116 260,100 260,330 0,340" fill="url(#poolRoom)"/>
      <polygon points="148,112 260,98 260,142" fill="var(--blue)"/>
      <polygon points="0,334 260,320 260,382 0,382" fill="var(--blue-light)"/>
      <polygon points="0,340 150,346 260,330 260,382 0,382" fill="var(--blue)"/>
      <polygon points="0,374 260,360 260,382 0,382" fill="var(--blue-deep)" opacity=".6"/>
    </svg>
    <div class="brand"><span class="dot"></span>Summit Realty</div>
    <div class="agent-mark">Dana Moretti</div>
    <p class="lifelong-note">Along with being your Realtor, I’m a lifelong resource for all things home-related &amp; beyond… if you need a great referral for anything at all, call me! I can’t wait to work with you!</p>
    <svg class="headshot" role="img" aria-label="Portrait photo of the agent" viewBox="0 0 102 142" preserveAspectRatio="none">
      <defs><linearGradient id="portrait" x1="0" y1="0" x2="0" y2="1"><stop offset="0" stop-color="#d9c39a"/><stop offset=".6" stop-color="#c9b7a4"/><stop offset="1" stop-color="#2a2a30"/></linearGradient></defs>
      <rect width="102" height="142" fill="url(#portrait)"/>
    </svg>
    <div class="agent-id">Dana Moretti<br>Realtor ®<br><span class="dre">DRE# 01234567</span></div>
    <p class="agent-invite">Please feel welcome to call me<br>for all things home related.<br>I will look forward to meeting you!</p>
    <ul class="contact">
      <li class="name">DANA MORETTI</li>
      <li><svg viewBox="0 0 10 10"><circle cx="5" cy="5" r="4.5" fill="none" stroke="#fff"/><path d="M3.4 3 l1 1 -.5.6 c.4.8.9 1.3 1.6 1.6 l.6-.5 1 1 -.7.8 c-1.8-.3-3.4-1.9-3.7-3.7z" fill="#fff"/></svg>555 010 4821</li>
      <li><svg viewBox="0 0 10 10"><circle cx="5" cy="5" r="4.5" fill="none" stroke="#fff"/><rect x="2.8" y="3.5" width="4.4" height="3" fill="none" stroke="#fff" stroke-width=".7"/><path d="M2.8 3.5 L5 5.3 7.2 3.5" fill="none" stroke="#fff" stroke-width=".7"/></svg>dana@danamhomes.com</li>
      <li><svg viewBox="0 0 10 10"><circle cx="5" cy="5" r="4.5" fill="none" stroke="#fff"/><circle cx="5" cy="5" r="2.4" fill="none" stroke="#fff" stroke-width=".7"/><path d="M2.6 5 H7.4 M5 2.6 V7.4" stroke="#fff" stroke-width=".6"/></svg>www.danamhomes.com</li>
    </ul>
    <div class="badges"><span></span><span></span></div>
  </section>

  <!-- front cover -->
  <section class="front-cover">
    <svg class="shapes" width="236" height="382" viewBox="0 0 236 382">
      <defs>
        <linearGradient id="nightHouse" x1="0" y1="0" x2="1" y2="1">
          <stop offset="0" stop-color="var(--photo-night-a)"/>
          <stop offset=".6" stop-color="#a07a4c"/>
          <stop offset="1" stop-color="#3f7fb8"/>
        </linearGradient>
      </defs>
      <polygon role="img" aria-label="Photo of a luxury home with pool at dusk" points="0,0 236,0 236,94 0,80" fill="url(#nightHouse)"/>
      <polygon points="0,76 150,96 0,110" fill="var(--blue)"/>
    </svg>
    <div class="front-mark">Dana Moretti</div>
    <h1 class="news-title">We've Got<br>News For You...</h1>
  </section>

  <!-- inside spread -->
  <div class="inside-photo">
    <svg role="img" aria-label="Photo of a Mediterranean-style community entrance with palms and fountain" viewBox="0 0 112 382" preserveAspectRatio="none">
      <defs><linearGradient id="palms" x1="0" y1="0" x2="0" y2="1"><stop offset="0" stop-color="var(--photo-palm-a)"/><stop offset=".45" stop-color="#c9b79a"/><stop offset=".8" stop-color="var(--photo-palm-b)"/><stop offset="1" stop-color="#8a9a6a"/></linearGradient></defs>
      <rect width="112" height="382" fill="url(#palms)"/>
    </svg>
  </div>

  <section class="inside-page">
    <article class="section intro">
      <h2>LET ME INTRODUCE MYSELF</h2>
      <p>I’m originally from Chicago, but I’m a full-fledged California girl now. I’ve lived and worked in Orange County since 1996. I always say where we live is the next best thing to living on a tropical island. I’ve traveled to many and I’m always happy to come back to my Laguna Niguel home.</p>
      <p>My passion for this area is why I’m in Real Estate. I consider myself incredibly fortunate to sell homes and help people purchase homes in an area that I love with all my heart.</p>
      <p>This passion also carries over in representing my clients with the highest degree of professionalism, enthusiasm and care. My business is built on exceptional customer service and I’m grateful my clients are mostly repeat and referrals.</p>
    </article>

    <article class="section tenet">
      <h2>MY CORE TENET</h2>
      <p>It’s All About YOU!<br>My #1 priority is understanding YOUR needs and YOUR objectives. This understanding, along with working diligently on your behalf, means we accomplish your goal whether you’re purchasing your 1st home or selling a home you’ve loved so you can move on to the next chapter of your life</p>
    </article>

    <article class="section services">
      <h2>REAL ESTATE SERVICES &amp; BEYOND...</h2>
      <p>Simply put, I help people who are local, relocating and investing, sell and purchase homes in Southern California. For purchases outside of California, I can refer to a network of agents across the country.<br>I also provide a team who is dedicated to providing outstanding customer service throughout the transaction. My team includes a network of lenders, title, and escrow officers, in house CPA, stagers, photographers, contractors and more.</p>
    </article>

    <article class="section selling">
      <h2>SELLING YOUR<br>HOME</h2>
      <p>Selling your home is not like any other business transaction. It’s also personal. My priority as your Listing Agent is to guide you through what can be a complicated and sometimes emotional process.</p>
      <p>I place great emphasis on marketing your property with professional photographs, along with harnessing the power of the Internet and the virtual world to reach as many buyers as possible. Your property will be marketed to the public as well as to other agents, thus creating maximum exposure of your home.</p>
      <p>When we first meet to discuss selling your home, it’s essential for me to gain an understanding of your unique needs such as timelines, expectations and financial considerations, just to name a few. From there, I begin the process of listing and marketing your home. I lead you through negotiations and more paperwork than you ever care to do, guiding you to the successful closing of your home.</p>
    </article>

    <article class="section buying">
      <h2>BUYING A<br>HOME</h2>
      <p>If you’re thinking about buying a home, it’s imperative you have an accomplished, real estate professional by your side to walk you through what is likely the largest purchase of your life.</p>
      <p>To get started, I like to meet with you so we have an opportunity to get to know each other as purchasing a home is a uniquely, personal endeavor. At that time, we can discuss your goals and if it’s a good time for you to purchase a home.</p>
      <p>From there, the first step is to obtain a pre-approval from a lender. I’m able to recommend various lenders who can introduce and explain the various loan products available.</p>
      <p>After you’ve been pre-approved, that’s when the fun starts! I guide you through the home buying adventure every step of the way and look forward to handing you the keys to your new home.</p>
    </article>

    <aside class="testimonials">
      <h2>TESTIMONIALS:</h2>
      <blockquote>Dana got us an amazing deal on our new home and sold our old home in a week. Dana is patient, hardworking, professional and most importantly HONEST. Dana is definitely one of the best in the business!<cite>Paige &amp; Aaron Lind</cite></blockquote>
      <blockquote>Dana is the kind of Real Estate professional everyone wants to represent them. She is knowledgeable, ethical, energetic, and follows up on every detail. Her honesty, integrity and expertise combined make her a very special and remarkable professional. We were lucky to find her!<cite>Howard &amp; Karen Miles</cite></blockquote>
      <blockquote>During the home buying process, Dana becomes your trusted advisor, mentor and friend. Her knowledge of the industry, community and market are best in class. A true professional! Dana aligned her goals with my own and understood the motivation behind my purchase. Dana is unequivocally the reason why I was able to purchase my home in Laguna Niguel and provide my family with a world-class community. Without her guidance and experience, I would still be in the market attempting to navigate the ever-changing world of real estate.<cite>Yasmin Carver</cite></blockquote>
    </aside>
  </section>

</div>
</body>
</html>
```